San Francisco Pet Care Non Profit

Business Card Design for non profit organization.
We are a mobile pet care team who supports and attends to pets whose owners are homeless. Thanks for your help and creativity.

Industry/Entity Type

Non Profit

Contact Information for Business Card

Marisol Keddy
President
2871 Larkmoor Street, #512
San Francisco, CA 94187
phone: 415-729-3846
fax: 415-781-4052
marisol@tidywagonvan.org
website: tidywagonvan.org
facebook: pawcircle.net/TidyWagonVan

Font styles to use
Serif
Sans Serif

Colors

Designer to choose colors to be used in the design.

Requirements
Must have
• above details and attached logo

```html
<!DOCTYPE html>
<html lang="en">
<head>
<meta charset="utf-8">
<title>TidyWagonVan Business Card</title>
<link href="https://fonts.googleapis.com/css2?family=Work+Sans:wght@400;500;600&display=swap" rel="stylesheet">
<style>
  :root {
    --page-bg: #e6e2dc;
    --card-bg: #f4f2ef;
    --card-edge: #d9d5cf;
    --band-dark: #2c2928;
    --teal: #1ea2bc;
    --teal-light: #5cc3d6;
    --ink: #3a3838;
    --ink-soft: #5c5a58;
    --white: #ffffff;
  }
  html, body {
    margin: 0;
    padding: 0;
    width: 1200px;
    height: 1047px;
    overflow: hidden;
    background: var(--page-bg);
    font-family: "Work Sans", Arial, sans-serif;
  }
  .business-card {
    position: absolute;
    left: 80px;
    top: 240px;
    width: 1040px;
    height: 566px;
    border-radius: 24px;
    background: var(--card-bg);
    box-shadow: 0 0 0 1px var(--card-edge), 0 10px 30px rgba(0,0,0,0.08);
    overflow: hidden;
  }
  .header-band {
    position: absolute;
    left: 0;
    top: 0;
    width: 1040px;
    height: 240px;
  }
  .holder {
    position: absolute;
    right: 47px;
    top: 52px;
    text-align: right;
  }
  .holder-name {
    margin: 0;
    font-size: 37px;
    font-weight: 500;
    letter-spacing: 2px;
    color: var(--teal);
    line-height: 1;
  }
  .holder-title {
    margin: 12px 0 0;
    font-size: 22px;
    letter-spacing: 1px;
    color: #d8d6d4;
    line-height: 1;
  }
  .brand {
    position: absolute;
    left: 46px;
    top: 140px;
  }
  .brand-row {
    display: flex;
    align-items: center;
    gap: 16px;
  }
  .brand-dot {
    width: 62px;
    height: 62px;
    border-radius: 50%;
    background: var(--teal);
  }
  .brand-name {
    font-size: 46px;
    font-weight: 600;
    color: var(--teal);
    line-height: 1;
  }
  .brand-tagline {
    margin: 4px 0 0 150px;
    font-size: 20px;
    font-weight: 600;
    color: var(--band-dark);
  }
  .divider {
    position: absolute;
    left: 43px;
    top: 328px;
    width: 950px;
    height: 2px;
    background: var(--teal);
  }
  .contact-list {
    position: absolute;
    left: 44px;
    top: 360px;
    margin: 0;
    padding: 0;
    list-style: none;
  }
  .contact-list li {
    display: flex;
    align-items: center;
    height: 33px;
    font-size: 24px;
    letter-spacing: 0.8px;
    color: var(--ink-soft);
  }
  .contact-icon {
    width: 16px;
    height: 16px;
    margin-right: 16px;
    flex: none;
  }
  .web-domain { color: var(--teal); }
  .address {
    position: absolute;
    right: 47px;
    top: 458px;
    margin: 0;
    text-align: right;
    font-style: normal;
    font-size: 24px;
    letter-spacing: 0.8px;
    line-height: 33px;
    color: var(--ink);
  }
</style>
</head>
<body>
  <div class="business-card">
    <svg class="header-band" viewBox="0 0 1040 240" aria-hidden="true">
      <path d="M0,0 H1040 V200 C860,214 700,186 560,128 C400,66 200,82 0,136 Z" fill="var(--band-dark)"/>
      <path d="M0,40 C200,8 400,40 560,108 C700,168 860,204 1040,192 L1040,212 C860,224 700,196 560,134 C400,70 200,58 0,92 Z" fill="var(--teal)"/>
      <path d="M0,30 C200,0 400,30 560,100 C700,160 860,196 1040,184" fill="none" stroke="var(--white)" stroke-width="3" opacity="0.7"/>
    </svg>

    <div class="holder">
      <p class="holder-name">MARISOL KEDDY</p>
      <p class="holder-title">President</p>
    </div>

    <div class="brand">
      <div class="brand-row">
        <span class="brand-dot"></span>
        <span class="brand-name">TidyWagonVan</span>
      </div>
      <p class="brand-tagline">Mobile Pet Care Team</p>
    </div>

    <div class="divider"></div>

    <ul class="contact-list">
      <li>
        <svg class="contact-icon" viewBox="0 0 16 16" aria-hidden="true"><path d="M3 1 L6 1 L7 5 L5 6.5 C6 9 7.5 10.5 9.5 11 L11 9 L15 10 L15 13 C15 14.5 14 15 12.5 15 C6 14.5 1.5 10 1 3.5 C1 2 1.5 1 3 1 Z" fill="var(--teal)"/></svg>
        415-729-3846
      </li>
      <li>
        <svg class="contact-icon" viewBox="0 0 16 16" aria-hidden="true"><rect x="4" y="1" width="8" height="4" fill="var(--teal)"/><rect x="1" y="6" width="14" height="6" rx="1.5" fill="var(--teal)"/><rect x="4" y="10" width="8" height="5" fill="var(--teal)" stroke="var(--card-bg)" stroke-width="1"/></svg>
        415-781-4052
      </li>
      <li>
        <svg class="contact-icon" viewBox="0 0 16 16" aria-hidden="true"><rect x="1.5" y="3.5" width="13" height="9" fill="none" stroke="var(--teal)" stroke-width="1.6"/><path d="M1.5 3.5 L8 9 L14.5 3.5" fill="none" stroke="var(--teal)" stroke-width="1.6"/></svg>
        marisol@tidywagonvan.org
      </li>
      <li>
        <svg class="contact-icon" viewBox="0 0 16 16" aria-hidden="true"><circle cx="8" cy="8" r="6.5" fill="none" stroke="var(--teal)" stroke-width="1.5"/><ellipse cx="8" cy="8" rx="2.8" ry="6.5" fill="none" stroke="var(--teal)" stroke-width="1.3"/><path d="M1.5 8 H14.5" stroke="var(--teal)" stroke-width="1.3"/></svg>
        <span>www.<span class="web-domain">tidywagonvan</span>.org</span>
      </li>
      <li>
        <svg class="contact-icon" viewBox="0 0 16 16" aria-hidden="true"><circle cx="8" cy="8" r="6" fill="var(--teal)"/></svg>
        pawcircle.net/TidyWagonVan
      </li>
    </ul>

    <address class="address">
      2871 Larkmoor Street, #512<br>
      San Francisco, CA 94187
    </address>
  </div>
</body>
</html>
```